Linden Hall College Needs an Event Flyer for Highly Visible Upcoming Event

Looking for an 8.5 in. x 11 in. flyer for an upcoming event at Linden Hall College.

The speaker is Rabbi Miriam Tolkow. Her title is Rabbi Simon Ravitch Professor of Jewish Religious Thought, Cedarbrook Seminary-Institute for Textual Studies.

The name of her talk is "Legal Imagination and the Question of Covenant Bonds."

Here is a brief description:
Classic Jewish law prescribes a model of marriage in which the woman is unilaterally acquired by the man and is, hence, unable to free herself should she wish to end the marriage. Drawing from her landmark book "Reweaving the Covenant," Rabbi Miriam Tolkow, a leading Jewish feminist theologian and scholar of Jewish law, will discuss how and why Jewish law should accommodate a more egalitarian vision of marital relationships and traditions.

The event will be held:
Thursday, February 13, 2014
7:30 p.m.
Founders Reading Room
Linden Hall College

The top of the flyer should contain this information:
Second in the Rabbi Nathan Orloff Lecture Series

The bottom of the flyer should contain:
1. Linden Hall College logo and Orloff Institute logo
2. Admission: $10 general admission; students free with ID.
3. Purchase tickets at lindenhallcollege.edu/tickets

Thank you!

Target Market(s)

Audience will be overwhelmingly Jewish. Age ranges from 20 to 70.

Industry/Entity Type

College

Requirements
Must have
• 1. Logos of Linden Hall College and Orloff Institute (attached)
• 2. Name of talk
• 3. Date, time, place
• 4. Cost and URL of where to buy ticket
• 5. That this event is the second in the Rabbi Nathan Orloff Lecture Series.
Nice to have
• Description of event (not at all necessary, though)

```html
<!DOCTYPE html>
<html lang="en">
<head>
<meta charset="utf-8">
<title>Legal Imagination and the Question of Covenant Bonds — Linden Hall College</title>
<link rel="stylesheet" href="https://fonts.googleapis.com/css2?family=Marcellus&family=Tinos:wght@400;700&family=Great+Vibes&family=Questrial&display=swap">
<style>
  :root {
    --ink: #1a1a1a;
    --band: #231f20;
    --gold: #f2c530;
    --rule: #f0c93a;
    --paper: #ffffff;
    --photo-light: #ece9e4;
    --photo-mid: #cfcac2;
    --brand: #2f5b94;
  }
  * { margin: 0; padding: 0; box-sizing: border-box; }
  html, body { width: 947px; height: 1200px; overflow: hidden; background: var(--paper); }
  .flyer { position: relative; width: 947px; height: 1200px; background: var(--paper); color: var(--ink); }

  .series-band {
    position: absolute; left: 40px; top: 35px; width: 83px; height: 1158px;
    background: var(--band); display: flex; align-items: center; justify-content: center;
  }
  .series-band__text {
    writing-mode: vertical-rl; transform: rotate(180deg);
    font-family: "Marcellus", serif; font-size: 27px; letter-spacing: 5.6px;
    color: var(--paper); white-space: nowrap;
  }

  .speaker-bar {
    position: absolute; left: 123px; top: 35px; width: 806px; height: 102px;
    background: var(--gold); text-align: center;
  }
  .speaker-bar__name {
    font-family: "Marcellus", serif; font-weight: 400; font-size: 31px; letter-spacing: 4px;
    margin-top: 22px; line-height: 1;
  }
  .speaker-bar__title {
    font-family: "Tinos", serif; font-weight: 700; font-size: 15.5px; margin-top: 14px;
  }

  .hero {
    position: absolute; left: 123px; top: 147px; width: 806px; height: 638px;
    background: radial-gradient(ellipse at 50% 40%, var(--photo-light) 0%, #e2ded8 55%, var(--photo-mid) 100%);
  }

  .talk-title {
    position: absolute; left: 123px; top: 455px; width: 806px; font-weight: 400;
  }
  .talk-title__script {
    font-family: "Great Vibes", cursive; font-weight: 400; color: #111; line-height: 0.95;
    display: block;
  }
  .talk-title__line1 { font-size: 128px; margin-left: 52px; }
  .talk-title__line2 { font-size: 112px; margin-left: 170px; margin-top: -52px; }
  .talk-title__sub {
    position: absolute; left: 82px; top: 232px;
    font-family: "Tinos", serif; font-weight: 400; font-size: 25px; letter-spacing: 1.2px; color: #222;
    white-space: nowrap;
  }

  .details { position: absolute; left: 205px; top: 820px; width: 392px; }
  .details__item {
    font-family: "Questrial", sans-serif; font-size: 26px; line-height: 1;
    padding: 4px 0 7px; border-bottom: 2px solid var(--rule);
  }
  .details__item + .details__item { margin-top: 4px; }
  .details__item--last { border-bottom: none; }

  .partners {
    position: absolute; left: 728px; top: 832px;
    display: flex; flex-direction: column; gap: 16px;
  }
  .partner {
    display: flex; align-items: center; gap: 10px;
    font-family: "Questrial", sans-serif; font-size: 21px; line-height: 1.05;
    color: var(--brand);
  }
  .partner__mark { width: 40px; height: 40px; background: var(--brand); flex: none; }

  .tickets {
    position: absolute; left: 205px; top: 1012px;
    font-family: "Questrial", sans-serif; font-size: 26px; line-height: 1.5;
  }
  .tickets__indent { padding-left: 175px; }
  .tickets__url { margin-top: 8px; }
</style>
</head>
<body>
  <main class="flyer">
    <aside class="series-band">
      <span class="series-band__text">SECOND IN THE RABBI NATHAN ORLOFF LECTURE SERIES</span>
    </aside>

    <header class="speaker-bar">
      <h2 class="speaker-bar__name">RABBI MIRIAM TOLKOW</h2>
      <p class="speaker-bar__title">Professor of Jewish Religious Thought • Cedarbrook Seminary-Institute for Textual Studies</p>
    </header>

    <div class="hero" role="img" aria-label="Close-up photograph of two wedding rings resting on an illuminated Hebrew marriage contract"></div>

    <h1 class="talk-title">
      <span class="talk-title__script talk-title__line1">Legal</span>
      <span class="talk-title__script talk-title__line2">Imagination</span>
      <span class="talk-title__sub">and the Question of Covenant Bonds</span>
    </h1>

    <section class="details">
      <p class="details__item">Thursday, February 13, 2014</p>
      <p class="details__item">7:30 p.m.</p>
      <p class="details__item">Founders Reading Room</p>
      <p class="details__item details__item--last">Linden Hall College</p>
    </section>

    <div class="partners">
      <div class="partner">
        <span class="partner__mark"></span>
        <span>Linden Hall<br>College</span>
      </div>
      <div class="partner">
        <span class="partner__mark"></span>
        <span>Orloff<br>Institute</span>
      </div>
    </div>

    <section class="tickets">
      <p>Admission: $10 general admission</p>
      <p class="tickets__indent">students free with ID.</p>
      <p class="tickets__url">Purchase tickets: lindenhallcollege.edu/tickets</p>
    </section>
  </main>
</body>
</html>
```